Programmierer für Automatisierung-Anlagen benötigt Corporate Design
Zielgruppe
Wir sind Programmierer für Automatisierung-Anlagen. Unser Schwerpunkt liegt auf Inbetriebnahmen von Produktionsanlagen mit Robotik.
Unsere Zielgruppe sind überwiegend männliche Angestellte aus dem mittleren Management.
Aufgabenstellung
Unser aktuelles Logo ist aus einem Portfolio und wurde nicht speziell für unser Unternehmen erstellt. Es gilt als Anhaltspunkt.
Das Logo soll unsere Zuverlässigkeit und unsere technischen Innovation (Informatik) hervorheben.

```html
<!DOCTYPE html>
<html lang="de">
<head>
<meta charset="utf-8">
<title>Velto Automation – Geschäftsausstattung</title>
<link href="https://fonts.googleapis.com/css2?family=Questrial&family=Open+Sans:wght@400&display=swap" rel="stylesheet">
<style>
  :root {
    --brand-blue: #4f4fcf;
    --dark-band: #4a4a4a;
    --text-gray: #4c4c4c;
    --light-text: #e8e8e8;
    --paper: #ffffff;
    --page-bg: #ffffff;
    --mark-gray: #9a9a9a;
  }
  * { margin: 0; padding: 0; box-sizing: border-box; }
  html, body { width: 888px; height: 1200px; overflow: hidden; background: var(--page-bg); }
  body { position: relative; font-family: "Questrial", sans-serif; color: var(--text-gray); }

  .sheet, .card { position: absolute; background: var(--paper); box-shadow: 4px 6px 14px rgba(0,0,0,0.22); overflow: hidden; }
  .top-band { position: absolute; left: 0; top: 0; right: 0; background: var(--brand-blue); }
  .bottom-band { position: absolute; left: 0; right: 0; bottom: 0; background: var(--dark-band); }
  .abs { position: absolute; }

  .wordmark { font-family: "Questrial", sans-serif; color: var(--brand-blue); white-space: nowrap; letter-spacing: 0.02em; display: flex; align-items: center; justify-content: center; }
  .wordmark .square { display: inline-block; background: var(--brand-blue); }
  .tagline { color: var(--text-gray); letter-spacing: 0.08em; white-space: nowrap; text-align: center; }

  .services { color: var(--brand-blue); white-space: nowrap; }

  .icon-line { position: absolute; display: flex; align-items: center; white-space: nowrap; }
  .icon-line svg { flex: none; }

  .web-tab { position: absolute; background: var(--brand-blue); color: #fff; display: flex; align-items: center; white-space: nowrap; border: 1.5px solid #fff; border-right: none; border-top: none; border-bottom-left-radius: 10px; }

  /* Letterhead */
  .letterhead { left: 160px; top: 85px; width: 559px; height: 790px; }
  .letterhead .top-band { height: 9px; }
  .letterhead .bottom-band { height: 44px; }
  .letterhead .logo-block { left: 352px; top: 90px; width: 186px; }
  .letterhead .wordmark { font-size: 15px; gap: 6px; }
  .letterhead .wordmark .square { width: 10px; height: 10px; }
  .letterhead .tagline { font-size: 5.5px; margin-top: 4px; }
  .letterhead .services { left: 362px; top: 124px; font-size: 9px; line-height: 10.8px; }
  .sender-line { left: 70px; top: 124px; font-family: "Open Sans", sans-serif; font-size: 6.6px; color: #333; white-space: nowrap; }
  .corner { position: absolute; width: 7px; height: 7px; border-color: var(--mark-gray); border-style: solid; border-width: 0; }
  .fold-mark { position: absolute; width: 7px; height: 0; border-top: 0.8px solid var(--mark-gray); }
  .letterhead .contact { font-size: 10.3px; }
  .letterhead .contact-line { left: 416px; gap: 6px; line-height: 10px; }
  .footer-col { position: absolute; top: 757px; padding-left: 5px; border-left: 0.8px solid var(--light-text); font-size: 7.8px; line-height: 8.6px; color: var(--light-text); white-space: nowrap; }
  .letterhead .web-tab { left: 394px; top: 740px; width: 166px; height: 18px; font-size: 13px; padding-left: 20px; gap: 4px; }

  /* Cards */
  .card { width: 284px; height: 184px; top: 940px; }
  .card .top-band { height: 8px; }
  .card .bottom-band { height: 14px; }
  .card-front { left: 143px; }
  .card-back { left: 456px; }
  .card-front .logo-block { left: 0; right: 0; top: 116px; }
  .card-front .wordmark { font-size: 17px; gap: 7px; }
  .card-front .wordmark .square { width: 11px; height: 11px; }
  .card-front .tagline { font-size: 6px; margin-top: 5px; }
  .card-back .logo-block { left: 154px; top: 64px; width: 126px; }
  .card-back .wordmark { font-size: 9.5px; gap: 4px; }
  .card-back .wordmark .square { width: 6px; height: 6px; }
  .card-back .tagline { font-size: 4px; margin-top: 3px; }
  .card-back .services { left: 10px; top: 56px; font-size: 5.6px; line-height: 7.5px; }
  .person-name { left: 10px; top: 105px; font-size: 11.5px; color: var(--brand-blue); font-family: "Questrial", sans-serif; -webkit-text-stroke: 0.3px var(--brand-blue); white-space: nowrap; }
  .person-role { left: 10px; top: 117px; font-size: 8.5px; white-space: nowrap; }
  .card-back .contact-line { font-size: 8.5px; gap: 5px; line-height: 9px; }
  .card-back .web-tab { left: 152px; top: 163px; width: 133px; height: 13px; font-size: 10.5px; padding-left: 7px; gap: 4px; }
</style>
</head>
<body>

<section class="sheet letterhead" aria-label="Briefbogen">
  <div class="top-band"></div>

  <div class="abs logo-block">
    <div class="wordmark"><span class="square"></span>VELTO AUTOMATION</div>
    <div class="tagline">PRÄZISE. SICHER. VERNETZT.</div>
  </div>

  <div class="abs services">
    | SPS-/ ROBOTERPROGRAMMIERUNG<br>
    | ELEKTRISCHE PLANUNG MIT CAD-SYSTEMEN<br>
    | HARDWARE-/SOFTWARE-ENGINEERING
  </div>

  <span class="corner" style="left:54px;top:119px;border-left-width:.8px;border-top-width:.8px;"></span>
  <span class="corner" style="left:273px;top:119px;border-right-width:.8px;border-top-width:.8px;"></span>
  <span class="corner" style="left:54px;top:230px;border-left-width:.8px;border-bottom-width:.8px;"></span>
  <span class="corner" style="left:273px;top:230px;border-right-width:.8px;border-bottom-width:.8px;"></span>
  <div class="abs sender-line">Velto Automation | Musterstrasse 123 | 12345 Musterstadt</div>

  <span class="fold-mark" style="left:0;top:279px;"></span>
  <span class="fold-mark" style="right:0;top:279px;"></span>
  <span class="fold-mark" style="left:0;top:558px;"></span>
  <span class="fold-mark" style="right:0;top:558px;"></span>

  <div class="contact">
    <div class="icon-line contact-line" style="top:670px;align-items:flex-start;">
      <svg width="7" height="10" viewBox="0 0 7 10"><path d="M3.5 9.5 C1.5 6.5 0.6 5 0.6 3.5 A2.9 2.9 0 0 1 6.4 3.5 C6.4 5 5.5 6.5 3.5 9.5Z" fill="none" stroke="var(--brand-blue)" stroke-width="1"/><circle cx="3.5" cy="3.5" r="1" fill="var(--brand-blue)"/></svg>
      <span>Musterstrasse 123<br>12345 Musterstadt</span>
    </div>
    <div class="icon-line contact-line" style="top:702px;">
      <svg width="9" height="9" viewBox="0 0 10 10"><path d="M2 0.5 L4 2.8 L3 4 C3.6 5.4 4.6 6.4 6 7 L7.2 6 L9.5 8 L8.3 9.5 C4.5 9.3 0.7 5.5 0.5 1.7Z" fill="var(--brand-blue)"/></svg>
      <span>0 12 34/ 12 34 56 78</span>
    </div>
    <div class="icon-line contact-line" style="top:714px;">
      <svg width="9" height="9" viewBox="0 0 10 10"><rect x="0.5" y="4" width="9" height="5.5" fill="var(--brand-blue)"/><rect x="2.5" y="0.5" width="5" height="3.5" fill="none" stroke="var(--brand-blue)" stroke-width="0.9"/><rect x="2" y="5.5" width="6" height="1" fill="#fff"/></svg>
      <span>0 12 34 / 12 34 56 78</span>
    </div>
    <div class="icon-line contact-line" style="top:726px;">
      <svg width="9" height="8" viewBox="0 0 10 8"><rect x="0.3" y="0.5" width="9.4" height="7" fill="var(--brand-blue)"/><path d="M0.5 0.8 L5 4.5 L9.5 0.8 M0.5 7.3 L3.8 3.8 M9.5 7.3 L6.2 3.8" stroke="#fff" stroke-width="0.8" fill="none"/></svg>
      <span>info@veltoautomation.de</span>
    </div>
  </div>

  <div class="bottom-band"></div>
  <div class="footer-col" style="left:47px;">Velto Automation<br>Geschäftsführer<br>Jonas Brenner</div>
  <div class="footer-col" style="left:133px;">Stadtbank Musterstadt<br>IBAN DE123456 0000 0000 0000 00<br>BIC MUSTER1ABC</div>
  <div class="footer-col" style="left:283px;">Amtsgericht Musterstadt<br>Finanzamt Musterstadt<br>Steuer-Nr.: 123/456 8900</div>

  <div class="web-tab">
    <svg width="11" height="11" viewBox="0 0 12 12"><g fill="none" stroke="#fff" stroke-width="0.8"><circle cx="6" cy="6" r="5.2"/><ellipse cx="6" cy="6" rx="2.4" ry="5.2"/><path d="M0.8 6 H11.2 M1.6 3.3 H10.4 M1.6 8.7 H10.4"/></g></svg>
    <span>veltoautomation.de</span>
  </div>
</section>

<section class="card card-front" aria-label="Visitenkarte Vorderseite">
  <div class="top-band"></div>
  <div class="abs logo-block">
    <div class="wordmark"><span class="square"></span>VELTO AUTOMATION</div>
    <div class="tagline">PRÄZISE. SICHER. VERNETZT.</div>
  </div>
  <div class="bottom-band"></div>
</section>

<section class="card card-back" aria-label="Visitenkarte Rückseite">
  <div class="top-band"></div>

  <div class="abs services">
    | SPS-/ ROBOTERPROGRAMMIERUNG<br>
    | ELEKTRISCHE PLANUNG MIT CAD-SYSTEMEN<br>
    | HARDWARE-/SOFTWARE-ENGINEERING
  </div>

  <div class="abs logo-block">
    <div class="wordmark"><span class="square"></span>VELTO AUTOMATION</div>
    <div class="tagline">PRÄZISE. SICHER. VERNETZT.</div>
  </div>

  <div class="abs person-name">Jonas Brenner</div>
  <div class="abs person-role">Geschäftsführer</div>

  <div class="icon-line contact-line" style="left:10px;top:144px;align-items:flex-start;">
    <svg width="6" height="9" viewBox="0 0 7 10"><path d="M3.5 9.5 C1.5 6.5 0.6 5 0.6 3.5 A2.9 2.9 0 0 1 6.4 3.5 C6.4 5 5.5 6.5 3.5 9.5Z" fill="none" stroke="var(--brand-blue)" stroke-width="1"/><circle cx="3.5" cy="3.5" r="1" fill="var(--brand-blue)"/></svg>
    <span>Musterstrasse 123<br>12345 Musterstadt</span>
  </div>

  <div class="icon-line contact-line" style="left:159px;top:117px;">
    <svg width="8" height="8" viewBox="0 0 10 10"><path d="M2 0.5 L4 2.8 L3 4 C3.6 5.4 4.6 6.4 6 7 L7.2 6 L9.5 8 L8.3 9.5 C4.5 9.3 0.7 5.5 0.5 1.7Z" fill="var(--brand-blue)"/></svg>
    <span>0 12 34/ 12 34 56 78</span>
  </div>
  <div class="icon-line contact-line" style="left:159px;top:128px;">
    <svg width="8" height="8" viewBox="0 0 10 10"><path d="M5 0.5 L9.5 5 L5 9.5 L0.5 5Z" fill="var(--brand-blue)"/></svg>
    <span>0171 / 12 34 56 789</span>
  </div>
  <div class="icon-line contact-line" style="left:159px;top:139px;">
    <svg width="8" height="8" viewBox="0 0 10 10"><rect x="0.5" y="4" width="9" height="5.5" fill="var(--brand-blue)"/><rect x="2.5" y="0.5" width="5" height="3.5" fill="none" stroke="var(--brand-blue)" stroke-width="0.9"/><rect x="2" y="5.5" width="6" height="1" fill="#fff"/></svg>
    <span>0 12 34 / 12 34 56 78</span>
  </div>
  <div class="icon-line contact-line" style="left:159px;top:150px;">
    <svg width="8" height="7" viewBox="0 0 10 8"><rect x="0.3" y="0.5" width="9.4" height="7" fill="var(--brand-blue)"/><path d="M0.5 0.8 L5 4.5 L9.5 0.8 M0.5 7.3 L3.8 3.8 M9.5 7.3 L6.2 3.8" stroke="#fff" stroke-width="0.8" fill="none"/></svg>
    <span>info@veltoautomation.de</span>
  </div>

  <div class="bottom-band"></div>
  <div class="web-tab">
    <svg width="9" height="9" viewBox="0 0 12 12"><g fill="none" stroke="#fff" stroke-width="0.9"><circle cx="6" cy="6" r="5.2"/><ellipse cx="6" cy="6" rx="2.4" ry="5.2"/><path d="M0.8 6 H11.2 M1.6 3.3 H10.4 M1.6 8.7 H10.4"/></g></svg>
    <span>veltoautomation.de</span>
  </div>
</section>

</body>
</html>
```